Law Firm Advertising Design Needed

Law Office of Dorvel K Tansy provides legal services to businesses and individuals who have been or are being injured. Our main practice area is personal injury (car accidents, wrongful death, premises liability), but we are looking for an ad that highlights a lesser known area of our practice - insurance company bad faith and breach of contract.

This ad will be placed in 8 1/2" x 11" format in a local neighborhood directory. It will also be placed in a smaller format (to be determined) in the local newspaper of a region of Arizona that has recently lost a considerable number of homes and people to wildfire.

We want to convey through the ad that our firm is available to help if their insurance company is not paying a legitimate claim or not paying enough for their claim.

Because of the tragic nature of the events in Yarnell, we would like to avoid images of fire or anything resembling fire. However, the ad should capture the attention of individuals who are struggling through an insurance claim with all the stacks of paperwork and frustrated with unresponsive adjusters and unreasonably low offers.

The design should convey a feeling of safety, security and being taken care of.

Information that must be included in the ad are: the firm name (Law Office of Dorvel K Tansy), address (4857 W 17th Avenue, Ste 406, Phoenix, AZ 85033), the phone number (602-574-2930) and the fact that we have mobile offices available to assist in your area.

An example of text that has been used in the past is here:
"If your own insurance company is refusing to pay what you are owed on a claim, call the Law Office of Dorvel K Tansy. We fight for you by examining the reasons your insurance carrier is denying or making an insufficient offer on the claim; updating and correcting claim documentation; making a new demand and filing a lawsuit if necessary. Whether it's a simple misunderstanding or something more complicated, we can help!

Here are a few of the kinds of claims we handle:
- Hit and Run or Uninsured driver claims
- Fire, flood and property loss
- Life insurance benefits
- Health insurance claims
- Catastrophic losses
- Business insurance
- Wrongful Death Benefits

Our attorneys are available to help you cut through the nonsense. Call to make an appointment for a free consultation with an attorney today. "

An example of a previous ad for car accident services is attached for reference.
Updates

Hi Everyone,

The main lawyer involved in the decision making process has been giving me some feedback in general on the designs that I thought I would pass along.  He does not want the name of the law firm to be the first thing you notice when you look at the ad. Try to keep that small and possibly to the bottom of the ad. The phone number should be rather large, but the address should be rather small (we are required by the State Bar to include our address, but we don't want our location to limit the location of our clients because our mobile offices can travel to them).  He would prefer that the logo either not be included or be not a significant part of the ad.

                                   

Thanks!  I will continue providing individual feedback to ads received. 

Target Market(s)

Low to middle income residents of the State of Arizona with little or no college education

Industry/Entity Type

Insurance

```html
<!DOCTYPE html>
<html lang="en">
<head>
<meta charset="utf-8">
<title>Law Office of Dorvel K Tansy – Insurance Claims</title>
<link rel="stylesheet" href="https://fonts.googleapis.com/css2?family=Tinos:wght@700&family=PT+Sans:wght@400;700&display=swap">
<style>
  :root {
    --band-top: #0a5a92;
    --band-bottom: #1488c2;
    --sky: #1596cc;
    --mid-blue: #0b6fb0;
    --navy: #0a2070;
    --deep-navy: #061550;
    --white: #ffffff;
    --gold: #f2b824;
    --paper: #d9dde2;
    --wood: #7a3a14;
    --book: #b89558;
    --heading-blue: #1578c4;
  }
  html, body {
    margin: 0;
    padding: 0;
    width: 927px;
    height: 1200px;
    overflow: hidden;
  }
  .ad {
    position: relative;
    width: 927px;
    height: 1200px;
    overflow: hidden;
    background:
      radial-gradient(ellipse 520px 260px at 470px 520px, var(--sky) 0%, rgba(21,150,204,0) 100%),
      linear-gradient(180deg, var(--mid-blue) 0%, var(--sky) 45%, var(--mid-blue) 70%, var(--navy) 88%, var(--deep-navy) 100%);
    font-family: "PT Sans", "Tahoma", sans-serif;
    color: var(--white);
  }
  .title-band {
    position: absolute;
    left: 0; top: 0;
    width: 927px; height: 173px;
    background: linear-gradient(180deg, var(--band-top) 0%, var(--band-bottom) 100%);
  }
  .headline {
    position: absolute;
    left: 0; top: 62px;
    width: 927px;
    margin: 0;
    text-align: center;
    font-family: "Tinos", "Times New Roman", serif;
    font-weight: 700;
    font-size: 62px;
    line-height: 1;
    letter-spacing: 0.5px;
  }
  .photo-strip {
    position: absolute;
    left: 0; top: 173px;
    width: 927px; height: 218px;
    background: var(--white);
  }
  .photo {
    position: absolute;
    top: 0; height: 218px;
  }
  .photo--contract { left: 0; width: 291px; background: linear-gradient(135deg, #f1f2f4 0%, var(--paper) 60%, #b9bec6 100%); }
  .photo--gavel { left: 305px; width: 302px; background: radial-gradient(ellipse at 50% 50%, #b36a2c 0%, var(--wood) 55%, #3e1a08 100%); }
  .photo--book { left: 622px; width: 305px; background: linear-gradient(180deg, #c9ced2 0%, #8d8f8e 45%, var(--book) 70%, #e4cf9e 100%); }
  .pitch {
    position: absolute;
    left: 0; top: 430px;
    width: 927px;
    text-align: center;
  }
  .pitch__line {
    margin: 0;
    font-size: 20px;
    line-height: 30px;
  }
  .pitch__call {
    margin: 4px 0 0;
    font-size: 22px;
    line-height: 30px;
    font-weight: 700;
  }
  .practice-heading {
    position: absolute;
    left: 0; top: 615px;
    width: 927px;
    margin: 0;
    text-align: center;
    font-weight: 700;
    font-size: 28px;
    letter-spacing: -1px;
    color: var(--heading-blue);
    -webkit-text-stroke: 5px var(--white);
    paint-order: stroke fill;
  }
  .practice-list {
    position: absolute;
    left: 0; top: 664px;
    width: 927px;
    margin: 0; padding: 0;
    list-style: none;
    text-align: center;
  }
  .practice-list li {
    font-size: 20px;
    line-height: 36.4px;
    letter-spacing: 0.3px;
  }
  .divider {
    position: absolute;
    left: 28px; top: 931px;
    width: 865px; height: 4px;
    background: var(--gold);
  }
  .brand {
    position: absolute;
    left: 230px; top: 1040px;
    display: flex;
    align-items: center;
    gap: 8px;
  }
  .brand__mark {
    width: 16px; height: 16px;
    background: var(--white);
  }
  .brand__name {
    font-size: 22px;
    font-weight: 700;
  }
  .contact {
    position: absolute;
    left: 420px; top: 972px;
    width: 325px;
    text-align: center;
    font-weight: 700;
  }
  .contact__firm {
    margin: 0;
    font-size: 17px;
    line-height: 28px;
    letter-spacing: 0.3px;
  }
  .contact__address {
    margin: 0;
    font-style: normal;
    font-size: 17px;
    line-height: 27px;
    letter-spacing: 0.4px;
  }
  .contact__phone {
    margin: 4px 0 0;
    font-size: 36px;
    line-height: 42px;
    letter-spacing: 1px;
  }
  .contact__web {
    margin: 0;
    font-size: 20px;
    line-height: 28px;
    letter-spacing: 0.8px;
  }
</style>
</head>
<body>
<main class="ad">
  <header class="title-band">
    <h1 class="headline">Let Us Fight For You!</h1>
  </header>

  <section class="photo-strip">
    <div class="photo photo--contract" role="img" aria-label="Photo of a contract document with a fountain pen"></div>
    <div class="photo photo--gavel" role="img" aria-label="Photo of a wooden gavel beside the scales of justice"></div>
    <div class="photo photo--book" role="img" aria-label="Photo of eyeglasses resting on an open law book"></div>
  </section>

  <section class="pitch">
    <p class="pitch__line">Got a problem with your Insurance Company?</p>
    <p class="pitch__line">Breach of Contract? Unreasonable Claims?</p>
    <p class="pitch__call">Call us! Mobile offices available to assist in your area.</p>
  </section>

  <h2 class="practice-heading">AREAS OF PRACTICE</h2>
  <ul class="practice-list">
    <li>Hit and Run or Uninsured driver claims</li>
    <li>Fire, flood and property loss</li>
    <li>Life insurance benefits</li>
    <li>Health insurance claims</li>
    <li>Catastrophic losses</li>
    <li>Business insurance</li>
    <li>Wrongful Death Benefits</li>
  </ul>

  <div class="divider"></div>

  <div class="brand">
    <span class="brand__mark"></span>
    <span class="brand__name">Tansy Law</span>
  </div>

  <section class="contact">
    <p class="contact__firm">Law Office of Dorvel K Tansy</p>
    <address class="contact__address">4857 W 17th Avenue, Ste 406<br>Phoenix, AZ 85033</address>
    <p class="contact__phone">602-574-2930</p>
    <p class="contact__web">www.tansylaw.com</p>
  </section>
</main>
</body>
</html>
```